ADA COMPLIANCE

We are in need of flyer or tri fold page for ada compliance, handicap ramps and parking lot striping.

Target Market(s)

Commercial Construction Industry

Industry/Entity Type

Parking

Font styles to use
Other font styles liked:
• Felix Titling

Colors
0355a3
acd036

Requirements
Must have
• Our Company Name and logo, 8004172593 number License #2837406
• List of services provided in uploaded images. Navy blue with high vizability green

```html
<!DOCTYPE html>
<html lang="en">
<head>
<meta charset="utf-8">
<title>Summit Construction Services – Tri-fold</title>
<link href="https://fonts.googleapis.com/css2?family=Oswald:wght@500;600&family=Cinzel:wght@400&family=Open+Sans:wght@400;600;700&family=Raleway:wght@300;400&display=swap" rel="stylesheet">
<style>
  :root{
    --navy:#0355a3;
    --green:#acd036;
    --brown:#5b3a1d;
    --paper:#f4f5f6;
    --ink:#222;
    --grey:#555;
  }
  html,body{margin:0;padding:0;overflow:hidden;background:var(--brown);}
  .canvas{position:relative;width:713px;height:1200px;background:var(--brown);font-family:"Open Sans",sans-serif;overflow:hidden;}
  .abs{position:absolute;}
  .panel-label{position:absolute;font-family:"Oswald",sans-serif;font-weight:500;color:#fff;font-size:20px;transform:translateX(-50%);white-space:nowrap;}
  .sheet{position:absolute;background:var(--paper);box-shadow:0 2px 6px rgba(0,0,0,.45);overflow:hidden;}
  .outside{left:20px;top:70px;width:669px;height:522px;}
  .inside{left:20px;top:618px;width:669px;height:520px;}

  /* outside flap */
  .flap-title{left:10px;top:20px;width:206px;font-family:"Oswald",sans-serif;font-weight:600;font-size:19px;color:var(--navy);letter-spacing:.3px;}
  .flap-copy{left:10px;width:206px;font-size:6.6px;line-height:1.55;color:var(--grey);text-align:justify;margin:0;}
  .phone-band{left:0;top:224px;width:222px;height:118px;background:var(--green);}
  .phone{position:absolute;left:0;width:222px;text-align:center;font-family:"Raleway",sans-serif;font-weight:400;color:var(--ink);}
  .phone-band .num{top:14px;font-size:23px;}
  .phone-band .free{top:44px;font-size:13px;}
  .phone-band .spec{position:absolute;left:0;top:72px;width:222px;text-align:center;font-weight:700;font-size:12px;line-height:1.35;color:var(--ink);}
  .service-list{left:8px;top:354px;width:206px;text-align:center;font-size:9.2px;line-height:1.5;color:var(--ink);margin:0;}

  /* back */
  .back-blue{left:222px;top:0;width:222px;height:222px;background:var(--navy);}
  .back-blue p{margin:0;padding:32px 10px 0;color:#fff;text-align:center;font-size:11.6px;line-height:1.6;}
  .ramp-strip{left:222px;top:240px;width:222px;height:87px;background:#e2e4e6;}
  .ramp-photo{left:284px;top:240px;width:160px;height:87px;background:linear-gradient(135deg,#b9bcbf,#e7e7e6 55%,#9c9ea0);}
  .access-icon{left:230px;top:244px;width:76px;height:76px;}
  .back-contact{left:222px;top:343px;width:222px;height:179px;background:var(--navy);color:#fff;text-align:center;}
  .brand{font-family:"Open Sans",sans-serif;font-weight:600;letter-spacing:1px;}
  .back-contact .brand{margin-top:50px;font-size:16px;color:#fff;}
  .back-contact .addr{margin-top:26px;font-size:8.4px;line-height:1.6;}
  .back-contact .web{margin-top:8px;font-size:14px;font-weight:700;letter-spacing:.5px;}

  /* front */
  .front-brand{left:444px;top:60px;width:225px;text-align:center;}
  .front-brand .mark{display:inline-block;width:14px;height:14px;background:var(--navy);margin-bottom:10px;}
  .front-brand .brand{font-size:17px;color:var(--navy);line-height:1.3;}
  .front-web{left:444px;top:184px;width:225px;text-align:center;font-weight:700;font-size:14px;color:var(--navy);letter-spacing:.5px;}
  .front-green{left:444px;top:224px;width:225px;height:118px;background:var(--green);}
  .front-title{left:460px;top:222px;width:186px;height:130px;background:var(--navy);color:#fff;font-family:"Cinzel",serif;font-size:23px;line-height:1.13;text-align:center;display:flex;align-items:center;justify-content:center;border-radius:0 0 3px 3px;}
  .license{left:444px;top:358px;width:225px;text-align:center;font-weight:700;font-size:8.4px;color:var(--ink);}
  .front-photo{left:464px;top:380px;width:182px;height:122px;border-radius:4px;background:linear-gradient(160deg,#8fa6b8,#c9c3b4 45%,#9b968b);}

  /* inside */
  .photo{position:absolute;border-radius:4px;box-shadow:0 1px 3px rgba(0,0,0,.35);}
  .inside-svg{left:0;top:0;}
  .stripe-title{left:200px;top:20px;font-family:"Oswald",sans-serif;font-weight:600;font-size:13.5px;color:var(--navy);white-space:nowrap;}
  .pave-title{left:44px;top:180px;font-family:"Oswald",sans-serif;font-weight:500;font-size:12px;color:#fff;letter-spacing:.2px;}
  .what-title{left:16px;top:212px;width:210px;font-weight:700;font-size:15.5px;line-height:1.3;color:var(--green);}
  .apply{left:16px;top:264px;font-weight:700;font-size:8.4px;color:#fff;}
  .paint-list{left:16px;top:283px;width:200px;margin:0;padding:0;list-style:none;}
  .paint-list li{position:relative;padding-left:15px;font-size:9.2px;line-height:15.2px;color:#fff;}
  .paint-list li::before{content:"";position:absolute;left:0;top:4px;width:7px;height:7px;border-radius:50%;background:var(--green);}
  .inside-bar{left:316px;top:480px;width:353px;height:20px;background:var(--green);}
  .inside-bar .num{position:absolute;left:16px;top:0;font-family:"Raleway",sans-serif;font-weight:300;font-size:14px;line-height:20px;color:#fff;}
  .inside-bar .web{position:absolute;right:12px;top:0;font-weight:700;font-size:11px;line-height:20px;color:#fff;letter-spacing:.4px;}
</style>
</head>
<body>
<div class="canvas">

  <div class="panel-label" style="left:124px;top:36px">Outside flap</div>
  <div class="panel-label" style="left:342px;top:36px">Back</div>
  <div class="panel-label" style="left:566px;top:36px">Front</div>

  <!-- OUTSIDE SHEET -->
  <section class="sheet outside">
    <!-- flap -->
    <h2 class="abs flap-title" style="margin:0">PARKING LOT STRIPING</h2>
    <p class="abs flap-copy" style="top:52px">Summit Construction Services, Inc is a full-service, architecture, engineering, interior design, turnkey property management, design-build and construction firm that delivers clients around California the highest quality solutions on time, on budget and above and beyond expectations.</p>
    <p class="abs flap-copy" style="top:134px">Summit Construction Services, Inc. has dramatically set new standards for design, quality and craftsmanship, efficient project management, cost containment and worker safety. We've integrated the building process from head to tail and adopted new technologies that bring state of the art design-build opportunities to clients and their communities.</p>
    <div class="abs phone-band">
      <div class="phone num">+1 800 417 2593</div>
      <div class="phone free">(FREEPHONE)</div>
      <div class="spec">There is nothing we cannot<br>do, but we specialize in:</div>
    </div>
    <p class="abs service-list">New Construction, Tenant Improvement, Building Alterations, Design/Build, Retail, Hotel, Casinos, Fueling Stations, Restaurants, Shopping Malls, Auto Facilities, Financial Institutions, Parking Structures, Custom Concrete, Foundations, ADA Improvements/Modifications, Framing, Drywall, Electrical, Plumbing, Flooring, Painting, Roofing...<br>And MORE!</p>

    <!-- back -->
    <div class="abs back-blue"><p>Summit Construction Services, Inc. is a full service General Contractor<br>and we have been serving Southern California since 2004. From the ground up to completion, Summit Construction Services, Inc. is your Best Choice for General Contracting Services!</p></div>
    <div class="abs ramp-strip"></div>
    <div class="abs ramp-photo" role="img" aria-label="Photo of a concrete sidewalk ramp with tactile warning strip"></div>
    <svg class="abs access-icon" viewBox="0 0 76 76" aria-label="Accessibility symbol">
      <rect x="1" y="1" width="74" height="74" rx="4" fill="#0355a3" stroke="#fff" stroke-width="2"/>
      <circle cx="34" cy="16" r="5" fill="#fff"/>
      <path d="M33 23 L35 40 L50 40 L56 56" fill="none" stroke="#fff" stroke-width="5" stroke-linecap="round" stroke-linejoin="round"/>
      <path d="M26 34 A15 15 0 1 0 46 52" fill="none" stroke="#fff" stroke-width="4"/>
    </svg>
    <div class="abs back-contact">
      <div class="brand">SUMMIT</div>
      <div class="addr">PO Box 482 Ontario CA 91761<br>info@summitbuildco.com</div>
      <div class="web">www.summitbuildco.com</div>
    </div>

    <!-- front -->
    <div class="abs front-brand">
      <span class="mark"></span>
      <div class="brand">SUMMIT<br>CONSTRUCTION SERVICES INC</div>
    </div>
    <div class="abs front-web">www.summitbuildco.com</div>
    <div class="abs front-green"></div>
    <h1 class="abs front-title" style="margin:0;font-weight:400">HANDICAP<br>RAMPS AND<br>PARKING<br>LOT STRIPING</h1>
    <div class="abs license">License Number &nbsp;#2837406</div>
    <div class="abs front-photo" role="img" aria-label="Photo of an accessible concrete ramp with handrails beside a building"></div>
  </section>

  <!-- INSIDE SHEET -->
  <section class="sheet inside">
    <svg class="abs inside-svg" width="669" height="520" viewBox="0 0 669 520">
      <defs>
        <linearGradient id="lot" x1="0" y1="0" x2="1" y2="1">
          <stop offset="0" stop-color="#8ea3a0"/>
          <stop offset=".35" stop-color="#3e4a57"/>
          <stop offset="1" stop-color="#2b3440"/>
        </linearGradient>
      </defs>
      <polygon points="0,0 190,0 168,46 375,46 250,175 0,175" fill="url(#lot)" role="img" aria-label="Photo of a large newly striped parking lot with accessible stalls"/>
      <polygon points="420,0 436,0 266,175 250,175" fill="#acd036"/>
      <polygon points="0,175 266,175 420,520 0,520" fill="#0355a3"/>
      <polygon points="250,175 266,175 298,240 282,240" fill="#acd036"/>
    </svg>
    <div class="photo" style="left:240px;top:46px;width:208px;height:116px;background:linear-gradient(150deg,#9ea4aa,#c2b9a6 50%,#6b6560)" role="img" aria-label="Photo of a freshly striped lot beside a building entrance"></div>
    <div class="abs stripe-title">PARKING LOT STRIPING</div>
    <div class="abs pave-title">COMPLETE PAVEMENT SERVICES</div>
    <div class="abs what-title">Parking lot Striping:<br>What exactly is it?</div>
    <div class="abs apply">The application of traffic paint to:</div>
    <ul class="abs paint-list">
      <li>Line Striping &amp; Stenciling</li>
      <li>Handicap ADA Striping</li>
      <li>Curb Paintinging</li>
      <li>Parking lot lines</li>
      <li>Handicap Logos</li>
      <li>Signs &amp; Poles</li>
      <li>Car Stops &amp; Bollards</li>
      <li>Game Courts</li>
      <li>Raised Pavment Markers</li>
      <li>Thermoplastics</li>
      <li>Pallet Striping</li>
      <li>Fire Lanes and No Parking zones</li>
      <li>Pretty much any marking on a<br>parking lot area</li>
    </ul>

    <div class="photo" style="left:240px;top:176px;width:208px;height:138px;background:linear-gradient(170deg,#b9a58a,#8f8f8f 45%,#2c323a 60%)" role="img" aria-label="Photo of striped accessible parking in front of a post office"></div>
    <div class="photo" style="left:240px;top:328px;width:208px;height:134px;background:linear-gradient(170deg,#c7d3dc,#8a9a72 30%,#3a4048 45%,#2c323a)" role="img" aria-label="Photo of rows of newly painted parking stalls"></div>
    <div class="photo" style="left:462px;top:24px;width:186px;height:138px;background:linear-gradient(170deg,#9fb8d6,#e0c25a 35%,#2d3440 55%)" role="img" aria-label="Photo of event parking with striped lanes beside tents"></div>
    <div class="photo" style="left:462px;top:176px;width:186px;height:138px;background:linear-gradient(170deg,#c8d4e0,#a7a39a 30%,#2c323a 45%)" role="img" aria-label="Photo of crew painting parking lot lines"></div>
    <div class="photo" style="left:462px;top:328px;width:186px;height:134px;background:linear-gradient(170deg,#d8dde2,#a9acae 40%,#8f8a6a)" role="img" aria-label="Photo of yellow floor striping in a warehouse"></div>

    <div class="abs inside-bar">
      <span class="num">+1 800 417 2593</span>
      <span class="web">www.summitbuildco.com</span>
    </div>
  </section>

  <div class="panel-label" style="left:120px;top:1148px">Inside Left</div>
  <div class="panel-label" style="left:340px;top:1148px">Inside &nbsp;Center</div>
  <div class="panel-label" style="left:562px;top:1148px">Inside Right</div>
</div>
</body>
</html>
```